Airborne Sensor Mfr Needs New Backdrop for Exhibition Booth

Our company manufacturers airborne hyperspectral and thermal cameras installed on drones and aircraft. Our customers work in numerous fields from forestry to oceanography, and from defense to oil & gas. We will be attending an airborne survey and mapping conference in a few months and want to try a new backdrop for the booth which will be about 3m x 3m. We are looking for something new and fresh with a high-tech but simple feel, professional and established but also friendly and inviting. Please see my below primitive draft design for some suggested text, images, and icons that I have in mind. Can you turn this into something really compelling that draws people to our booth? Or do you have some new ideas to build on my design? Look forward to seeing what you can do!
https://obvela.com/

```html
<!DOCTYPE html>
<html lang="en">
<head>
<meta charset="utf-8">
<title>Obvela Airborne Sensors – Booth Backdrop</title>
<link href="https://fonts.googleapis.com/css2?family=League+Spartan:wght@700;800&family=Poppins:wght@500;600&display=swap" rel="stylesheet">
<style>
  :root{
    --paper:#ffffff;
    --ink:#1c1c22;
    --label:#2b2a36;
    --sky:#5aa0c2;
    --navy:#2e3592;
    --icon:#5b3a9e;
    --accent:#e8265a;
    --footer:#414141;
    --band-1:#5cc0d4;
    --band-2:#2e3a96;
    --band-3:#7b3da0;
    --band-4:#e0377a;
    --band-5:#ee2a3c;
  }
  *{margin:0;padding:0;box-sizing:border-box}
  html,body{width:1200px;height:1200px;overflow:hidden;background:var(--paper)}
  .backdrop{position:relative;width:1200px;height:1200px;background:var(--paper);overflow:hidden;font-family:'Poppins',sans-serif}
  .brand{position:absolute;top:96px;left:0;width:1200px;display:flex;justify-content:center;align-items:center;gap:16px}
  .brand-dot{width:22px;height:22px;border-radius:50%;background:var(--navy)}
  .brand-name{font-family:'League Spartan',sans-serif;font-weight:800;font-size:76px;line-height:1;color:var(--ink);letter-spacing:2px}
  .headline{position:absolute;top:222px;left:0;width:1200px;text-align:center;font-family:'League Spartan',sans-serif;font-weight:800;font-size:103px;line-height:1;letter-spacing:1px}
  .headline .airborne{color:var(--sky)}
  .headline .sensors{color:var(--navy)}
  .hero{position:absolute;top:0;left:0;width:1200px;height:800px}
  .question{position:absolute;top:698px;left:0;width:1200px;text-align:center;font-family:'League Spartan',sans-serif;font-weight:800;font-size:49px;color:#fff;letter-spacing:.5px;line-height:1}
  .uses{position:absolute;top:820px;left:0;width:1200px;height:240px}
  .use{position:absolute;width:190px;margin-left:-95px;text-align:center;color:var(--label);font-weight:600;font-size:18.5px;line-height:23px}
  .use svg{display:block;margin:0 auto 6px;width:54px;height:54px;fill:var(--icon)}
  .row-1{top:0}
  .row-2{top:124px}
  .footer-band{position:absolute;left:0;top:1118px;width:1200px;height:82px;background:var(--footer)}
  .site{position:absolute;left:368px;top:1084px;width:464px;height:66px;border:2px solid #3a3a3a;border-radius:33px;background:var(--paper);display:flex;align-items:center;justify-content:center;font-family:'Poppins',sans-serif;font-weight:500;font-size:40px;letter-spacing:2px;color:var(--ink)}
  .site b{color:var(--accent);font-weight:600}
</style>
</head>
<body>
<main class="backdrop">
  <header class="brand">
    <span class="brand-dot"></span>
    <span class="brand-name">OBVELA</span>
  </header>

  <h1 class="headline"><span class="airborne">AIRBORNE</span> <span class="sensors">SENSORS</span></h1>

  <svg class="hero" viewBox="0 0 1200 800" aria-hidden="false">
    <defs>
      <linearGradient id="bandGrad" x1="0" x2="1" y1="0" y2="0">
        <stop offset="0" stop-color="var(--band-1)"/>
        <stop offset="0.3" stop-color="var(--band-2)"/>
        <stop offset="0.5" stop-color="var(--band-3)"/>
        <stop offset="0.75" stop-color="var(--band-4)"/>
        <stop offset="1" stop-color="var(--band-5)"/>
      </linearGradient>
      <linearGradient id="droneGrad" x1="0" y1="0" x2="0" y2="1">
        <stop offset="0" stop-color="#c9ccd0"/><stop offset="1" stop-color="#8d8f91"/>
      </linearGradient>
      <linearGradient id="mapGrad" x1="0" y1="0" x2="1" y2="1">
        <stop offset="0" stop-color="#d05ad8"/><stop offset="0.4" stop-color="#6a3fd0"/>
        <stop offset="0.7" stop-color="#e03aa8"/><stop offset="1" stop-color="#5a48c8"/>
      </linearGradient>
      <linearGradient id="heliGrad" x1="0" y1="0" x2="0" y2="1">
        <stop offset="0" stop-color="#9ea6a6"/><stop offset="0.6" stop-color="#c0a9a0"/><stop offset="1" stop-color="#e59a80"/>
      </linearGradient>
    </defs>
    <rect class="band" x="0" y="417" width="1200" height="358" fill="url(#bandGrad)"/>
    <polygon points="110,351 444,351 406,666 66,666" fill="#fff"/>
    <polygon points="116,356 439,356 402,661 72,661" fill="url(#droneGrad)" role="img" aria-label="Photo of an unmanned helicopter drone carrying a sensor pod on its landing gear"/>
    <polygon points="459,351 792,351 753,666 416,666" fill="#fff"/>
    <polygon points="464,356 787,356 748,661 422,661" fill="url(#mapGrad)" role="img" aria-label="False-colour hyperspectral image of terrain with mineral signatures"/>
    <polygon points="818,351 1142,351 1105,666 764,666" fill="#fff"/>
    <polygon points="823,356 1136,356 1100,661 770,661" fill="url(#heliGrad)" role="img" aria-label="Photo of a helicopter in flight against a sunset sky"/>
  </svg>

  <p class="question">WHAT DO YOU WANT&nbsp; TO DETECT &amp; MONITOR?</p>

  <section class="uses">
    <div class="use row-1" style="left:140px">
      <svg viewBox="0 0 54 54"><rect x="6" y="20" width="10" height="32"/><rect x="20" y="24" width="10" height="28"/><rect x="32" y="36" width="18" height="16"/><circle cx="12" cy="10" r="6"/><circle cx="22" cy="8" r="5"/><circle cx="32" cy="9" r="6"/></svg>
      Gas<br>Detection</div>
    <div class="use row-1" style="left:306px">
      <svg viewBox="0 0 54 54"><polygon points="18,2 4,38 16,38 16,50 20,50 20,38 32,38"/><polygon points="40,14 28,44 38,44 38,52 42,52 42,44 52,44"/></svg>
      Forestry</div>
    <div class="use row-1" style="left:468px">
      <svg viewBox="0 0 54 54"><path d="M27 4 C19 18 13 26 13 35 a14 14 0 0 0 28 0 C41 26 35 18 27 4z"/></svg>
      Water<br>Quality</div>
    <div class="use row-1" style="left:674px">
      <svg viewBox="0 0 54 54"><path d="M2 10 C18 6 32 14 30 36 C16 38 4 28 2 10z"/><path d="M52 22 C40 20 32 28 34 42 C46 42 52 34 52 22z"/></svg>
      Vegetation<br>Health</div>
    <div class="use row-1" style="left:871px">
      <svg viewBox="0 0 54 54"><circle cx="27" cy="27" r="11"/><circle cx="27" cy="27" r="19" fill="none" stroke="var(--icon)" stroke-width="4"/><rect x="25" y="2" width="4" height="10"/><rect x="25" y="42" width="4" height="10"/><rect x="2" y="25" width="10" height="4"/><rect x="42" y="25" width="10" height="4"/></svg>
      Precision<br>Ag</div>
    <div class="use row-1" style="left:1044px">
      <svg viewBox="0 0 54 54"><path d="M8 50 L46 6" stroke="var(--icon)" stroke-width="3" fill="none"/><ellipse cx="18" cy="30" rx="5" ry="11" transform="rotate(-40 18 30)"/><ellipse cx="28" cy="20" rx="5" ry="11" transform="rotate(-40 28 20)"/><ellipse cx="30" cy="38" rx="5" ry="11" transform="rotate(50 30 38)"/><ellipse cx="40" cy="28" rx="5" ry="11" transform="rotate(50 40 28)"/></svg>
      Species<br>Classification</div>

    <div class="use row-2" style="left:140px">
      <svg viewBox="0 0 54 54"><rect x="8" y="4" width="24" height="46" rx="3"/><path d="M40 26 C36 34 33 38 33 42 a7 7 0 0 0 14 0 C47 38 44 34 40 26z"/></svg>
      Pollution /<br>Disaster</div>
    <div class="use row-2" style="left:306px">
      <svg viewBox="0 0 54 54"><circle cx="27" cy="29" r="21" fill="none" stroke="var(--icon)" stroke-width="4"/><circle cx="27" cy="29" r="12" fill="none" stroke="var(--icon)" stroke-width="4"/><circle cx="27" cy="29" r="4"/><path d="M27 29 L12 10" stroke="var(--icon)" stroke-width="3"/></svg>
      Target<br>Detection</div>
    <div class="use row-2" style="left:468px">
      <svg viewBox="0 0 54 54"><path d="M4 40 L16 36 L34 40 L48 34 L50 38 L34 48 L14 46 L4 50z"/><rect x="26" y="14" width="3" height="22"/><ellipse cx="20" cy="16" rx="7" ry="4"/><ellipse cx="35" cy="10" rx="7" ry="4"/></svg>
      Environmental<br>Monitoring</div>
    <div class="use row-2" style="left:674px">
      <svg viewBox="0 0 54 54"><circle cx="27" cy="28" r="18"/><circle cx="12" cy="18" r="8"/><circle cx="42" cy="18" r="8"/><circle cx="10" cy="6" r="4"/><text x="27" y="33" text-anchor="middle" font-family="Poppins,sans-serif" font-weight="600" font-size="14" fill="#fff">CO₂</text></svg>
      Geology /<br>Mineral Exploration</div>
    <div class="use row-2" style="left:871px">
      <svg viewBox="0 0 54 54"><path d="M12 6 q-5 7 0 14 q5 7 0 14" fill="none" stroke="var(--icon)" stroke-width="3"/><path d="M22 6 q-5 7 0 14 q5 7 0 14" fill="none" stroke="var(--icon)" stroke-width="3"/><path d="M32 6 q-5 7 0 14 q5 7 0 14" fill="none" stroke="var(--icon)" stroke-width="3"/><path d="M42 6 q-5 7 0 14 q5 7 0 14" fill="none" stroke="var(--icon)" stroke-width="3"/><rect x="4" y="42" width="46" height="8"/></svg>
      Thermal<br>Anomalies</div>
    <div class="use row-2" style="left:1044px">
      <svg viewBox="0 0 54 54"><polygon points="18,2 4,46 16,46 16,52 20,52 20,46 30,46"/><path d="M38 20 C32 30 28 36 28 42 a10 10 0 0 0 20 0 C48 36 44 30 38 20z"/></svg>
      Wildfire /<br>Hotspot</div>
  </section>

  <div class="footer-band"></div>
  <div class="site">www.<b>obvela</b>.com</div>
</main>
</body>
</html>
```